Facebook Cover & Profile Branding for VelbrooK Systems

We need a modern, premium Facebook cover image for our company Velbrook Systems GmbH. The design should be clean, professional, and aligned with our corporate colors (neon green and deep blue) as well as our logo. It should clearly represent us as a technology and IT consulting company with a strong focus on software testing and quality assurance.

Since Velbrook Systems is also active in the U.S. market, the design may include global or U.S.-related elements (e.g., subtle references to international presence, tech innovation with a global reach).

Requirements:

Integration of the Velbrook logo and brand colors

Modern, premium look with a tech-driven feel

Clear, simple layout that looks good on desktop and mobile

Optional: subtle U.S./international references to highlight our global presence

Goal:
A professional, eye-catching Facebook cover image that strengthens our brand identity and reflects our international expansion into the U.S. market.

Target Market(s)

Medium to large enterprises in the technology, finance, and energy sectors - Companies looking for premium IT consulting, software testing, and quality assurance services - Decision makers and executives (CIOs, CTOs, IT managers) in Europe and the United States - A global audience that values innovation, professionalism, and trust

Industry/Entity Type

Information Technology & Consulting Software Testing & Quality Assurance Technology / Professional Services Global IT Consulting with U.S. Market Presence

Requirements
Must have
• Integration of the Velbrook Systems logo and brand colors (Neon Green & Deep Blue) Modern, premium design with a strong tech-oriented look and feel Clean and professional layout, optimized for both desktop and mobile display Clear visibility of the brand identity (technology, IT consulting, software testing, quality assurance) Subtle reference to U.S. presence / global expansion (to highlight activity in both Germany and the U.S.) Balanced use of colors and space for a high-end, corporate appearance
Nice to have
• Subtle animations or motion effects (e.g., light gradients, moving lines, glowing accents) Dark/Light version option for different moods or seasonal campaigns Integration of social media icons (LinkedIn, Instagram, Facebook) in a clean, minimal way Tech-inspired background elements (digital patterns, abstract shapes, network grids) Space for an optional tagline or slogan (e.g., “Innovation. Quality. Global Impact.”) Adaptability for other platforms (so the design style can be reused for LinkedIn or Twitter headers)
Should not have
• Cluttered or overloaded layouts that reduce clarity Low-quality stock photos or generic imagery that doesn’t fit a premium brand Use of colors outside the Velbrook brand identity (Neon Green & Deep Blue) Outdated design styles (e.g., heavy gradients, 3D effects, drop shadows) Complex text blocks that make the design look busy Elements that distract from the logo and core brand message Pop-art or playful styles that don’t match the premium, professional tech look

```html
<!DOCTYPE html>
<html lang="en">
<head>
<meta charset="utf-8">
<title>Velbrook Systems – Facebook Branding Set</title>
<link rel="stylesheet" href="https://fonts.googleapis.com/css2?family=Archivo:wdth,wght@62..125,100..900&family=Montserrat:wght@500;600&family=Outfit:wght@400;500&display=swap">
<style>
  :root {
    --board: #e3e3e3;
    --label: #2b2b2b;
    --ink: #2a2b2e;
    --ink-deep: #232427;
    --neon: #2fe026;
    --neon-soft: #3b7a37;
    --blue: #0a62f5;
    --blue-deep: #1e3f8c;
    --white: #ffffff;
    --tech-blue: #c9d8ff;
    --tech-green: #d9f5d2;
    --font-display: "Archivo", "Arial Black", sans-serif;
    --font-text: "Outfit", "Helvetica Neue", sans-serif;
    --font-label: "Montserrat", "Helvetica Neue", sans-serif;
  }
  * { box-sizing: border-box; margin: 0; padding: 0; }
  html, body { width: 1200px; height: 1101px; overflow: hidden; }
  body { background: var(--board); position: relative; font-family: var(--font-text); }

  .board-label {
    position: absolute;
    font-family: var(--font-label);
    font-weight: 600;
    font-size: 22px;
    letter-spacing: 2.2px;
    color: var(--label);
    transform: translateX(-50%);
    white-space: nowrap;
  }
  .label-profile { left: 332px; top: 44px; }
  .label-post { left: 867px; top: 44px; }
  .label-cover { left: 600px; top: 1037px; }

  /* Profile picture */
  .profile-avatar {
    position: absolute;
    left: 123px; top: 129px;
    width: 418px; height: 418px;
    border-radius: 50%;
    background:
      radial-gradient(circle at 0% 55%, rgba(40,70,150,.45), transparent 45%),
      linear-gradient(100deg, var(--ink) 0 50%, var(--ink-deep) 50% 100%);
    display: flex; align-items: center; justify-content: center;
  }
  .profile-avatar .brand-name { font-size: 46px; }

  /* Shared brand marker */
  .brand { display: flex; align-items: center; gap: 10px; position: absolute; }
  .brand-dot { width: 26px; height: 26px; border-radius: 50%; background: var(--neon); flex: none; }
  .brand-name {
    font-family: var(--font-text);
    font-weight: 500;
    color: var(--white);
    white-space: nowrap;
    line-height: 1;
  }

  /* Panels */
  .panel {
    position: absolute;
    overflow: hidden;
    background:
      radial-gradient(ellipse 45% 60% at 100% 0%, rgba(60,140,55,.95), rgba(60,140,55,0) 70%),
      radial-gradient(ellipse 55% 55% at 0% 75%, rgba(35,70,160,.6), transparent 70%),
      var(--ink);
    box-shadow: 0 22px 22px -14px rgba(0,0,0,.45);
  }
  .panel-post { left: 615px; top: 85px; width: 505px; height: 506px; }
  .panel-cover { left: 80px; top: 620px; width: 1040px; height: 395px; }

  .wave-field {
    position: absolute; left: 0; right: 0; bottom: 0;
    background:
      radial-gradient(ellipse 60% 80% at 70% 100%, rgba(70,150,190,.55), transparent 70%),
      radial-gradient(ellipse 70% 70% at 20% 110%, rgba(40,90,190,.6), transparent 70%);
  }
  .panel-post .wave-field { height: 150px; }
  .panel-cover .wave-field { height: 200px; }

  .headline { position: absolute; font-family: var(--font-display); font-weight: 900; font-stretch: 112%; line-height: 1; letter-spacing: -1px; white-space: nowrap; }
  .headline-white { color: var(--white); }
  .headline-tech {
    background: linear-gradient(90deg, var(--tech-blue), var(--white) 45%, var(--tech-green));
    -webkit-background-clip: text; background-clip: text; color: transparent;
  }
  .headline .accent-dot { color: var(--neon); }

  .enabling-box {
    position: absolute;
    border: 1.5px solid var(--neon);
    border-radius: 6px;
    background: linear-gradient(180deg, rgba(80,82,88,.85), rgba(55,57,62,.85));
    display: flex; align-items: center;
  }
  .enabling-box .headline { position: static; }

  /* Post specifics */
  .panel-post .brand { left: 173px; top: 66px; gap: 8px; }
  .panel-post .brand-dot { width: 18px; height: 18px; }
  .panel-post .brand-name { font-size: 17px; }
  .post-empowering { left: 0; right: 0; text-align: center; top: 140px; font-size: 33px; }
  .post-technology { left: 0; right: 0; text-align: center; top: 174px; font-size: 44px; }
  .post-enabling { left: 88px; top: 229px; width: 224px; height: 51px; padding-left: 24px; }
  .post-enabling .headline { font-size: 32px; }
  .post-success { left: 183px; top: 298px; font-size: 42px; }
  .post-subline {
    position: absolute; left: 0; right: 0; top: 356px;
    text-align: center; color: var(--white);
    font-size: 19px; line-height: 25px; font-weight: 400;
  }
  .post-cta { position: absolute; left: 103px; top: 435px; height: 36px; display: flex; }
  .cta-reach, .cta-phone {
    height: 36px; display: flex; align-items: center;
    font-family: var(--font-text); font-weight: 500; letter-spacing: -.3px;
  }
  .cta-reach {
    width: 135px; padding-left: 27px; background: var(--blue); color: var(--white); font-size: 17px;
    clip-path: polygon(8px 0, 100% 0, calc(100% - 8px) 100%, 0 100%);
  }
  .cta-phone {
    width: 175px; margin-left: -6px; padding-left: 18px; gap: 7px;
    background: var(--neon); color: #103a10; font-size: 14px;
    clip-path: polygon(8px 0, 100% 0, calc(100% - 8px) 100%, 0 100%);
  }

  /* Cover specifics */
  .panel-cover .brand { left: 62px; top: 104px; gap: 12px; }
  .panel-cover .brand-dot { width: 30px; height: 30px; }
  .panel-cover .brand-name { font-size: 30px; }
  .cover-empowering { left: 517px; top: 58px; font-size: 48px; }
  .cover-technology { left: 445px; top: 108px; font-size: 62px; }
  .cover-enabling { left: 447px; top: 193px; width: 333px; height: 76px; padding-left: 36px; }
  .cover-enabling .headline { font-size: 48px; }
  .cover-success { left: 585px; top: 290px; font-size: 62px; }
</style>
</head>
<body>
  <div class="board-label label-profile">PROFILE PICTURE</div>
  <div class="board-label label-post">FACEBOOK POST</div>

  <div class="profile-avatar">
    <span class="brand-name">Velbrook</span>
  </div>

  <section class="panel panel-post">
    <div class="wave-field" role="img" aria-label="Glowing blue particle wave landscape"></div>
    <div class="brand"><span class="brand-dot"></span><span class="brand-name">Velbrook Systems GmbH</span></div>
    <div class="headline headline-white post-empowering">EMPOWERING</div>
    <div class="headline headline-tech post-technology">TECHNOLOGY.</div>
    <div class="enabling-box post-enabling"><span class="headline headline-white">ENABLING</span></div>
    <div class="headline headline-white post-success">SUCCESS<span class="accent-dot">.</span></div>
    <p class="post-subline">Excellent software quality.<br>Globally minded.</p>
    <div class="post-cta">
      <span class="cta-reach">Reach Us!</span>
      <span class="cta-phone">
        <svg width="13" height="13" viewBox="0 0 24 24" aria-hidden="true"><path fill="#103a10" d="M6.6 10.8a15.1 15.1 0 0 0 6.6 6.6l2.2-2.2c.3-.3.7-.4 1-.2 1.1.4 2.3.6 3.6.6.6 0 1 .4 1 1V20c0 .6-.4 1-1 1A17 17 0 0 1 3 4c0-.6.4-1 1-1h3.5c.6 0 1 .4 1 1 0 1.3.2 2.5.6 3.6.1.3 0 .7-.2 1z"/></svg>
        +49 3000 55120-48
      </span>
    </div>
  </section>

  <section class="panel panel-cover">
    <div class="wave-field" role="img" aria-label="Glowing blue particle wave landscape"></div>
    <div class="brand"><span class="brand-dot"></span><span class="brand-name">Velbrook Systems GmbH</span></div>
    <div class="headline headline-white cover-empowering">EMPOWERING</div>
    <div class="headline headline-tech cover-technology">TECHNOLOGY.</div>
    <div class="enabling-box cover-enabling"><span class="headline headline-white">ENABLING</span></div>
    <div class="headline headline-white cover-success">SUCCESS<span class="accent-dot">.</span></div>
  </section>

  <div class="board-label label-cover">FACEBOOK COVER BANNER</div>
</body>
</html>
```